Business card

We are looking for a creative person to deigns our company business card.

Target Market(s)

College age student

Industry/Entity Type

Accommodation

Contact Information for Business Card

We want a fun, clean and sophisticated design. It should look good, but more importantly the information should be legible.

Font styles to use
Serif
Sans Serif
Other font styles liked:
• Open Sans ,

Colors
33a6d7

Requirements
Must have
• Must have a young and memorable message. Be legible.
• Our logo on the back on a solid blue , please find color and logo attached
• LodgeBridgely.net on the back.
Nice to have
• I would like to have couple of different fonts on the LodgeBridgely.net on the back of the cards with a solid blue.

```html
<!DOCTYPE html>
<html lang="en">
<head>
<meta charset="UTF-8">
<title>LodgeBridgely Business Card</title>
<link rel="stylesheet" href="https://fonts.googleapis.com/css2?family=Open+Sans:wght@400;600;700&display=swap">
<style>
  :root {
    --brand-blue: #3597d6;
    --accent-blue: #2b7fc3;
    --deep-navy: #17568f;
    --ink: #2c3440;
    --muted-ink: #4a5563;
    --card-white: #ffffff;
    --backdrop: #e9ebee;
  }
  * { margin: 0; padding: 0; box-sizing: border-box; }
  html, body {
    width: 1200px;
    height: 892px;
    overflow: hidden;
    background: var(--backdrop);
    font-family: "Open Sans", Arial, sans-serif;
  }
  .sheet {
    width: 1200px;
    height: 892px;
    display: flex;
    align-items: center;
    justify-content: center;
    gap: 60px;
  }
  .card {
    position: relative;
    width: 520px;
    height: 297px;
    overflow: hidden;
    box-shadow: 0 6px 18px rgba(20, 40, 70, 0.18);
  }

  /* Front side */
  .card--front { background: var(--card-white); }
  .holder {
    position: absolute;
    left: 30px;
    top: 24px;
  }
  .holder__name {
    font-size: 20px;
    font-weight: 400;
    color: var(--accent-blue);
    line-height: 1.2;
  }
  .holder__title {
    font-size: 15px;
    color: var(--ink);
    line-height: 1.3;
    padding-bottom: 5px;
    border-bottom: 2px solid var(--deep-navy);
    display: inline-block;
    padding-right: 20px;
  }
  .contact-list {
    list-style: none;
    margin-top: 8px;
  }
  .contact-list__item {
    display: flex;
    align-items: center;
    gap: 9px;
    font-size: 12.5px;
    color: var(--muted-ink);
    line-height: 22px;
  }
  .contact-list__icon {
    width: 13px;
    height: 13px;
    flex: none;
    fill: var(--deep-navy);
  }
  .front-mark {
    position: absolute;
    right: 34px;
    top: 178px;
    display: flex;
    align-items: center;
    gap: 8px;
    font-size: 16px;
    font-weight: 700;
    color: var(--deep-navy);
  }
  .front-mark__square {
    width: 14px;
    height: 14px;
    background: var(--deep-navy);
  }
  .front-stripe {
    position: absolute;
    left: 0;
    right: 0;
    top: 238px;
    height: 4px;
    background: var(--brand-blue);
  }
  .front-band {
    position: absolute;
    left: 0;
    right: 0;
    top: 248px;
    bottom: 0;
    background: var(--deep-navy);
  }

  /* Back side */
  .card--back {
    background: var(--brand-blue);
    display: flex;
    flex-direction: column;
    align-items: center;
    justify-content: center;
    gap: 12px;
  }
  .back-mark {
    display: flex;
    align-items: center;
    gap: 12px;
    font-size: 32px;
    font-weight: 700;
    color: var(--card-white);
  }
  .back-mark__square {
    width: 24px;
    height: 24px;
    background: var(--card-white);
  }
  .back-tagline {
    font-size: 15px;
    font-weight: 400;
    color: var(--card-white);
    letter-spacing: 0.3px;
  }
</style>
</head>
<body>
<main class="sheet">
  <section class="card card--front" aria-label="Business card front">
    <div class="holder">
      <p class="holder__name">Dana Whitfield</p>
      <p class="holder__title">Managing Director</p>
      <ul class="contact-list">
        <li class="contact-list__item">
          <svg class="contact-list__icon" viewBox="0 0 16 16" aria-hidden="true"><path d="M3.6 1.2l2.3 2.6-1.3 1.8c.9 2.1 2.4 3.6 4.5 4.6l1.8-1.3 2.7 2.3-1.3 2.3C7 13.2 2.6 8.9 1.3 2.5z"/></svg>
          <span>+15550148832</span>
        </li>
        <li class="contact-list__item">
          <svg class="contact-list__icon" viewBox="0 0 16 16" aria-hidden="true"><path d="M4 1h8v4H4zM1 6h14v6h-3v3H4v-3H1zm4 4v4h6v-4z"/></svg>
          <span>+5550148833</span>
        </li>
        <li class="contact-list__item">
          <svg class="contact-list__icon" viewBox="0 0 16 16" aria-hidden="true"><path d="M1 3h14v10H1zm1.5 1.5v.4L8 8.6l5.5-3.7v-.4zm0 2.2v4.8h11V6.7L8 10.4z"/></svg>
          <span>dwhitfield@lodgebridgely.net</span>
        </li>
        <li class="contact-list__item">
          <svg class="contact-list__icon" viewBox="0 0 16 16" aria-hidden="true"><path d="M8 1a7 7 0 100 14A7 7 0 008 1zm0 1.5c.8 0 1.7 1.6 2 4H6c.3-2.4 1.2-4 2-4zM5.9 7.9h4.2c0 .1 0 2-.1 2.1H6c-.1-.1-.1-2-.1-2.1zM2.6 6.5h2c0 .4-.1.9-.1 1.4s0 1.2.1 1.7h-2a5.6 5.6 0 010-3.1zm8.8 0h2a5.6 5.6 0 010 3.1h-2c.1-.5.1-1.1.1-1.7s0-1-.1-1.4zM6 11h4c-.3 1.6-1.1 2.5-2 2.5S6.3 12.6 6 11z"/></svg>
          <span>www.lodgebridgely.net</span>
        </li>
        <li class="contact-list__item">
          <svg class="contact-list__icon" viewBox="0 0 16 16" aria-hidden="true"><path d="M8 1a5 5 0 00-5 5c0 3.6 5 9 5 9s5-5.4 5-9a5 5 0 00-5-5zm0 7a2 2 0 110-4 2 2 0 010 4z"/></svg>
          <span>72 Maple Row, Boulder, CO 80302</span>
        </li>
      </ul>
    </div>
    <div class="front-mark">
      <span class="front-mark__square" aria-hidden="true"></span>
      <span>LodgeBridgely</span>
    </div>
    <div class="front-stripe"></div>
    <div class="front-band"></div>
  </section>

  <section class="card card--back" aria-label="Business card back">
    <div class="back-mark">
      <span class="back-mark__square" aria-hidden="true"></span>
      <span>LodgeBridgely.net</span>
    </div>
    <p class="back-tagline">Find your place. Live your campus life.</p>
  </section>
</main>
</body>
</html>
```